Graphic Design Project

We make rose petal jelly from old fashioned english roses. The jelly is sweet eaten with scones and clotted cream or as a filling in a victoria sandwich, as a topping on ice cream or thick set yogurt.
The image of the product is luxurious and decadent and very english.
We need a design for a label which has a picture of an old fashioned rose (rosa mundi or a compte de chambard) The rose must stand out clearly so the jelly is not confused with other fruit jams. The overall colour of the label should be pink and soft, with white or dark pink writing. The label needs to be fridge proof.

We also need a security strip to fit on the lid of the jar.

We need the following information on the label.
Name of our company-"Petal Lantern"
Name of Product-"Rose Petal Jelly"
Sales pitch-"With whole petals-a taste of summer, delicious on scones, as a filling in sponge cake, as a topping on ice cream or yogurt."
INGREDIENTS: Sugar, water, rose petals, lemon juice, natural jelling agent (agar-agar)
STORAGE: Store in a cool dry place, once opened keep refrigerated and consume within 4 weeks.
BEST BEFORE: See base

200g
Produced by:
PETAL LANTERN
The Brambles
Marsh Lane
Ashcombe
Gloucestershire
GL19 4QT
The label must have room for a bar code. The size of label approx 8-10cm long 5cm wide.
Updates

Hi

Just been looking at the Greville and Hartley site and the labels they have there have the up market feel I am trying to convey. Hope that helps, its classy but not twee.

Thanks

Thanks for all submissions. I would be grateful if you googled images for 'Colourful and expensive biscuits at Greville Hartley' The designs on the tins are the image we are trying to create. The colours are quite strong.

Thanks

Target Market(s)

older well off people who visit garden centres

Industry/Entity Type

Security

Requirements
Must have
• All writen info above and picture of old fashioned rose prferably rose a mundi. Luxury feel, very english, to appeal to older market
Pink colour sheme
Should not have
• dark or manly colours

```html
<!DOCTYPE html>
<html lang="en">
<head>
<meta charset="utf-8">
<title>Petal Lantern Rose Petal Jelly Label</title>
<link rel="stylesheet" href="https://fonts.googleapis.com/css2?family=Sorts+Mill+Goudy&display=swap">
<style>
  :root {
    --label-lilac: #bb80c2;
    --panel-white: #ffffff;
    --blush-text: #f6c6ee;
    --magenta: #c4158a;
    --wine: #8c1150;
    --weight-red: #a3124d;
    --rose-red: #d8213b;
    --rose-deep: #9e0f2a;
    --leaf-green: #7fae2a;
    --ink: #000000;
    --box-line: #333333;
  }
  * { margin: 0; padding: 0; box-sizing: border-box; }
  html, body { width: 1200px; height: 750px; overflow: hidden; background: var(--panel-white); }
  body { font-family: "Sorts Mill Goudy", Georgia, serif; }

  .label { position: relative; width: 1200px; height: 750px; }

  .front-panel {
    position: absolute; left: 0; top: 0; width: 797px; height: 750px;
    background: var(--label-lilac); text-align: center;
  }
  .brand-name {
    position: absolute; left: 0; width: 100%; top: 28px;
    font-size: 56px; font-weight: 400; color: var(--blush-text); line-height: 1;
  }
  .product-name {
    position: absolute; left: 0; width: 100%; top: 106px;
    font-size: 72px; font-weight: 400; color: var(--magenta); line-height: 1;
  }
  .tagline {
    position: absolute; left: 0; width: 100%; top: 197px;
    font-size: 25px; color: var(--blush-text);
  }
  .rose-illustration {
    position: absolute; left: 247px; top: 254px; width: 324px; height: 304px;
  }
  .serving-ideas {
    position: absolute; left: 0; width: 100%; top: 578px;
    font-size: 32px; line-height: 41px; color: var(--blush-text);
  }
  .net-weight {
    position: absolute; left: 607px; top: 694px;
    font-size: 36px; color: var(--weight-red);
  }

  .info-panel {
    position: absolute; left: 815px; top: 28px; width: 380px;
    color: var(--wine);
  }
  .info-block { font-size: 21px; line-height: 28px; margin-bottom: 36px; }
  .info-block.best-before { margin-bottom: 42px; }
  .producer { font-size: 29px; line-height: 35px; }

  .barcode-space {
    position: absolute; left: 1000px; top: 636px; width: 175px; height: 89px;
    border: 1.5px solid var(--box-line); border-radius: 3px;
    font-family: Arial, Helvetica, sans-serif; font-size: 18px; line-height: 24px;
    color: var(--ink); padding: 18px 0 0 6px;
  }
</style>
</head>
<body>
<div class="label">
  <section class="front-panel">
    <h2 class="brand-name">Petal Lantern</h2>
    <h1 class="product-name">Rose Petal Jelly</h1>
    <p class="tagline">"With whole petals its a taste of summer”</p>

    <svg class="rose-illustration" viewBox="0 0 324 304" role="img" aria-label="Illustration of a red old fashioned rose stem with two open blooms, buds and green leaves">
      <defs>
        <radialGradient id="roseTone" cx="55%" cy="35%" r="70%">
          <stop offset="0%" stop-color="var(--rose-red)"/>
          <stop offset="55%" stop-color="var(--rose-deep)" stop-opacity="0.75"/>
          <stop offset="100%" stop-color="var(--leaf-green)" stop-opacity="0.55"/>
        </radialGradient>
      </defs>
      <rect width="324" height="304" rx="20" fill="url(#roseTone)"/>
    </svg>

    <p class="serving-ideas">Delicious on scones, as a filling<br>in sponge cake, as a topping<br>on ice cream or yogurt.</p>
    <p class="net-weight">200g</p>
  </section>

  <section class="info-panel">
    <p class="info-block ingredients">INGREDIENTS:<br>Sugar, water, rose petals, lemon<br>juice, natural jelling agent (agar-agar)</p>
    <p class="info-block storage">STORAGE: Store in a cool dry<br>place, once opened keep refrigerated<br>and consume within 4 weeks.</p>
    <p class="info-block best-before">BEST BEFORE:<br>See base</p>
    <address class="producer" style="font-style: normal;">
      Produced by:<br>PETAL LANTERN<br>The Brambles<br>Marsh Lane<br>Ashcombe<br>Gloucestershire<br>GL19 4QT
    </address>
  </section>

  <div class="barcode-space">Bar<br>Code</div>
</div>
</body>
</html>
```